Professional Single Page Website Design for Vellowind Advisory

Vellowind Advisory is a new business consultancy specializing in providing expert services to small businesses, primarily in the brick-and-mortar retail and food service sectors. We offer a range of services including franchise development and launch, due diligence, and construction management.

Currently, we have a basic website set up at www.vellowindadvisory.example, but we need a professional touch to enhance its design and functionality.

Project Requirements:
- Single Page Design: For now, we need a single page design that effectively showcases who we are, our services, and contact information.
- Future Expansion: The design should be flexible and scalable for future expansion to include additional pages like specific service offerings, about us, and a dedicated contact page.
- Design Aesthetic: We are looking for a modern yet professional design that aligns with our brand identity.
- Logo: We have a logo that we like, which was also sourced from Pixel Forum. The logo files are attached to this project brief.

Key Sections to Include:
- Hero Section: An engaging introduction to Vellowind Advisory with a strong visual impact.
- About Us: A brief overview of who we are and our mission.
- Team: Section for the profiles of the two principals.
- Services: A clear and concise presentation of our services, including franchise development, due diligence, and construction management.
- Contact Information: Easy-to-find contact details, including a form for inquiries.
- Call to Action: Encouraging visitors to get in touch with us for consultations or further information.

Design Considerations:
- Ensure the design is responsive and mobile-friendly.
- Include high-quality images and icons that complement our services and industry.
- We do not need development services, this is only a design project.

```html
<!DOCTYPE html>
<html lang="en">
<head>
<meta charset="utf-8">
<title>Vellowind Advisory</title>
<link href="https://fonts.googleapis.com/css2?family=Poppins:wght@300;400;500;600;700&display=swap" rel="stylesheet">
<style>
:root{
  --mint:#8fc5a8;
  --mint-soft:#a9d3bc;
  --mint-pale:#dcefe4;
  --ink:#1d2733;
  --navy:#25313d;
  --navy-deep:#1b252f;
  --text:#3a4450;
  --white:#ffffff;
}
*{margin:0;padding:0;box-sizing:border-box}
html,body{width:1200px;height:4669px;overflow:hidden}
body{font-family:"Poppins",sans-serif;color:var(--text);background:var(--white);position:relative}
section,header,footer{position:absolute;left:0;width:1200px}
.abs{position:absolute}
.eyebrow{font-size:14px;letter-spacing:1.5px;text-transform:uppercase;font-weight:500;color:var(--ink)}
.h2{font-size:40px;font-weight:700;color:var(--ink);line-height:1.1}
.h2 span{color:var(--mint)}
.center{text-align:center;left:0;width:1200px}
.brand{font-size:22px;font-weight:600;color:var(--ink);display:flex;align-items:center;gap:12px;line-height:24px}
.brand i{display:block;flex:none;width:58px;height:58px;border:4px solid var(--mint);border-radius:50%}

/* hero */
.hero{top:0;height:707px;overflow:hidden}
.hero-photo{position:absolute;inset:0;background:linear-gradient(180deg,#d9e3ea 0%,#c6d3dc 35%,#8a9aa6 62%,#4c5964 80%,#2f3a44 100%)}
.nav{position:absolute;top:18px;left:130px;right:105px;display:flex;align-items:center;white-space:nowrap}
.nav .brand{font-size:20px;line-height:22px}
.nav ul{list-style:none;display:flex;margin-left:70px;font-size:15px;color:var(--ink)}
.nav li{padding:0 26px;border-left:1px solid #8d98a2;line-height:14px}
.nav li:first-child{border:none}
.nav li.active{border-bottom:3px solid var(--mint);padding-bottom:8px;margin-top:11px}
.btn{display:inline-block;background:var(--mint);color:var(--ink);border-radius:30px;font-size:15px;font-weight:500;white-space:nowrap}
.nav .btn{margin-left:auto;padding:13px 32px}
.hero-box{position:absolute;left:280px;top:133px;width:630px;height:158px;border:3px solid var(--mint)}
.hero-title{position:absolute;top:110px;left:0;width:1200px;text-align:center;font-size:40px;font-weight:700;line-height:44px;color:var(--ink)}
.hero-title span{color:var(--mint);font-size:48px;display:block}
.hero-sub{position:absolute;top:218px;width:1200px;text-align:center;font-size:19px;font-weight:500;color:var(--ink)}
.hero .btn.small{position:absolute;left:522px;top:266px;padding:9px 28px;font-size:14px}

/* who */
.who{top:707px;height:560px}
.who-photo{position:absolute;left:118px;top:100px;width:462px;height:462px}
.who-lead{position:absolute;left:617px;top:130px;width:500px;font-size:17.5px;font-weight:600;color:var(--ink);line-height:27px}
.who-body{position:absolute;left:620px;top:232px;width:505px;font-size:16.5px;line-height:24.6px}

/* mission */
.mission{top:1250px;height:432px;overflow:hidden;background:linear-gradient(180deg,#3b4a5a,#24303c 60%,#2b3744)}
.mission .eyebrow{color:#dfe6ec;left:128px;top:198px}
.mission .h2{color:#fff;left:126px;top:222px}
.mission-rule{left:392px;top:200px;width:1px;height:130px;background:#6d7a86}
.mission p{left:438px;top:195px;width:650px;font-size:16.5px;line-height:24.6px;color:#e7edf1}

/* team */
.team{top:1682px;height:557px;background:var(--mint)}
.team .eyebrow{color:#f2faf5;top:68px}
.team .h2{color:#fff;top:90px}
.card{position:absolute;width:386px;height:252px;background:#fff;box-shadow:6px 6px 0 -1px var(--mint),7px 7px 0 0 #fff}
.card-photo{position:absolute;width:176px;height:203px;top:22px;background:linear-gradient(180deg,#9fb5c3,#6e7f89 60%,#cfd6da)}
.card h3{position:absolute;font-size:20px;font-weight:700;color:var(--ink)}
.card .role{position:absolute;font-size:17px;color:var(--text)}
.card p{position:absolute;font-size:10.5px;line-height:17.5px;width:225px;color:var(--text)}
.dots{position:absolute;display:flex;gap:18px}
.dots i{width:15px;height:15px;border-radius:50%;border:2px solid var(--mint)}

/* services */
.services{top:2239px;height:1387px}
.timeline{left:600px;top:270px;width:2px;height:880px;background:var(--mint)}
.diamond{position:absolute;width:72px;height:72px;transform:rotate(45deg);border-radius:14px;background:var(--mint)}
.diamond.dark{background:var(--navy)}
.diamond::after{content:"";position:absolute;inset:22px;border:2.5px solid #fff;border-radius:50%}
.ring{position:absolute;border-radius:50%;border:2px solid var(--mint-soft)}
.circle-img{position:absolute;border-radius:50%}
.svc h3{position:absolute;font-size:22px;font-weight:600;color:var(--ink);line-height:27px}
.svc p{position:absolute;font-size:12.6px;line-height:19.2px}

/* contact */
.contact{top:3626px;height:722px;overflow:hidden;background:linear-gradient(180deg,#2e3a46,#1f2a34)}
.contact .eyebrow{color:var(--mint);top:94px}
.contact .h2{color:#fff;top:118px}
.info{position:absolute;left:160px;display:flex;gap:30px;align-items:center}
.info .ic{width:62px;height:62px;border-radius:50%;background:var(--mint);display:flex;align-items:center;justify-content:center}
.info h4{font-size:17px;font-weight:500;color:#fff}
.info span{font-size:17px;color:var(--mint);line-height:23px;display:block}
.form{position:absolute;left:573px;top:214px;width:520px;height:382px;background:var(--mint);border-radius:46px 0 46px 0}
.field{position:absolute;background:#fff;font-size:12px;color:#5a6470;padding:12px 18px;height:40px}
.form .send{position:absolute;left:48px;top:290px;width:170px;height:44px;border-radius:24px;background:var(--navy-deep);color:#fff;font-size:13px;font-weight:600;display:flex;align-items:center;justify-content:center}

/* footer */
.footer{top:4348px;height:321px;background:#fff}
.vrule{position:absolute;top:0;width:1px;height:180px;background:#d8dde1}
.footer h5{position:absolute;top:64px;font-size:18px;font-weight:600;color:var(--ink)}
.footer ul{position:absolute;list-style:none;font-size:12.5px;line-height:23.5px;color:var(--ink)}
.frow{position:absolute;display:flex;align-items:center;gap:10px;font-size:12.5px;color:var(--ink);white-space:nowrap}
.frow i{width:28px;height:28px;border-radius:50%;background:var(--mint);display:block;flex:none}
.social{position:absolute;left:950px;top:116px;display:flex;gap:22px}
.social i{width:26px;height:26px;border-radius:50%;background:var(--mint);display:block}
</style>
</head>
<body>

<header class="hero">
  <div class="hero-photo" role="img" aria-label="Photo of a modern two-storey office building with glass facade and parking lot under a cloudy sky"></div>
  <nav class="nav">
    <div class="brand"><i></i>Vellowind<br>Advisory</div>
    <ul>
      <li class="active">Home</li><li>About</li><li>Services</li><li>Team</li><li>Contact</li>
    </ul>
    <a class="btn">Get in touch</a>
  </nav>
  <div class="hero-box"></div>
  <h1 class="hero-title">Building Success in<span>Southern California</span></h1>
  <p class="hero-sub">Expertise at Every Step: From Planning to Execution</p>
  <a class="btn small">Learn More ›</a>
  <svg class="abs" style="left:0;top:600px" width="1200" height="107" viewBox="0 0 1200 107">
    <polygon points="0,107 0,95 600,22 600,107" fill="#fff"/>
    <polygon points="0,95 600,22 600,30 0,107" fill="#8fc5a8"/>
    <rect x="599" y="20" width="2" height="77" fill="#8fc5a8"/>
    <circle cx="600" cy="99" r="5" fill="#8fc5a8"/>
  </svg>
  <svg class="abs" style="left:590px;top:475px" width="20" height="30" viewBox="0 0 20 30"><rect x="1" y="1" width="18" height="28" rx="9" fill="none" stroke="#fff" stroke-width="2"/></svg>
</header>

<section class="who">
  <div class="eyebrow abs center" style="top:20px;text-align:center">Vellowind Advisory</div>
  <h2 class="h2 abs center" style="top:40px;text-align:center">Who We <span>Are</span></h2>
  <svg class="who-photo" viewBox="0 0 462 462" role="img" aria-label="Photo of a tall blue glass office tower seen from below">
    <defs><linearGradient id="sky" x1="0" y1="0" x2="1" y2="1"><stop offset="0" stop-color="#cfe3f2"/><stop offset=".5" stop-color="#3f7fc4"/><stop offset="1" stop-color="#1f4f93"/></linearGradient></defs>
    <rect x="81" y="81" width="300" height="300" rx="80" transform="rotate(45 231 231)" fill="none" stroke="#8fc5a8" stroke-width="12"/>
    <rect x="104" y="104" width="254" height="254" rx="62" transform="rotate(45 231 231)" fill="url(#sky)"/>
  </svg>
  <p class="who-lead">Welcome to Vellowind Advisory, your trusted partner in navigating the complexities of the real estate and small business markets.</p>
  <p class="who-body">Founded by industry veterans Marco Delaney and Evan Park, we specialize in providing comprehensive services tailored to the unique needs of our clients. Whether you're a franchisee, a new restaurant owner, or a commercial real estate investor, our expertise in due diligence, construction management, and investment property evaluation ensures you make informed, strategic decisions. Discover how Vellowind Advisory can support your business journey. Partner with us and experience the difference our dedication and expertise can make.</p>
</section>

<section class="mission" role="img" aria-label="Darkened photo of a low commercial building at dusk">
  <svg class="abs" style="left:0;top:0" width="1200" height="110" viewBox="0 0 1200 110">
    <polygon points="0,0 1200,0 1200,4 600,98 0,0" fill="#fff"/>
    <polygon points="0,0 600,98 600,106 0,16" fill="#8fc5a8"/>
  </svg>
  <div class="eyebrow abs">Vellowind Advisory</div>
  <h2 class="h2 abs">Our Mission</h2>
  <div class="mission-rule abs"></div>
  <p class="abs">At Vellowind Advisory, we are committed to your success. Our approach combines meticulous analysis, strategic insights, and personalized service to help you achieve your business goals. We pride ourselves on our ability to deliver results that exceed expectations, fostering long-term relationships built on trust and excellence.</p>
</section>

<section class="team">
  <div class="eyebrow abs center" style="text-align:center">Leadership Team</div>
  <h2 class="h2 abs center" style="text-align:center">Meet the Team</h2>
  <div class="card" style="left:187px;top:196px">
    <div class="card-photo" style="left:-91px" role="img" aria-label="Portrait photo of principal Marco Delaney"></div>
    <h3 style="left:110px;top:30px">Marco Delaney</h3>
    <div class="role" style="left:110px;top:56px">Principal</div>
    <p style="left:110px;top:92px">Marco Delaney brings almost 20 years of rich experience as a real estate investor and a pivotal role at one of southern California's largest real estate management firms, where he...</p>
    <div class="dots" style="left:112px;top:192px"><i></i><i></i><i></i></div>
  </div>
  <div class="card" style="left:700px;top:196px">
    <div class="card-photo" style="left:-89px" role="img" aria-label="Portrait photo of principal Evan Park"></div>
    <h3 style="left:110px;top:30px">Evan Park</h3>
    <div class="role" style="left:110px;top:56px">Principal</div>
    <p style="left:110px;top:92px">Evan Park is a seasoned real estate expert with extensive experience in project and construction management, and a licensed real estate agent in California. Fluent in both English and Korean.</p>
    <div class="dots" style="left:112px;top:192px"><i></i><i></i><i></i></div>
  </div>
  <div class="abs" style="left:605px;top:520px;width:2px;height:37px;background:#3a4450"></div>
</section>

<section class="services">
  <div class="abs" style="left:605px;top:0;width:2px;height:24px;background:#3a4450"></div>
  <div class="abs" style="left:600px;top:22px;width:12px;height:12px;border-radius:50%;background:#3a4450"></div>
  <div class="eyebrow abs center" style="top:80px;text-align:center">What we do</div>
  <h2 class="h2 abs center" style="top:102px;text-align:center">Vellowind <span>Services</span></h2>
  <div class="timeline abs"></div>

  <div class="svc">
    <div class="ring" style="left:150px;top:205px;width:372px;height:372px"></div>
    <div class="circle-img" style="left:164px;top:219px;width:344px;height:344px;background:radial-gradient(circle,#7fb0c2,#2c4a5c 55%,#15222d)" role="img" aria-label="Illustration of a hand holding a glowing globe with a storefront icon"></div>
    <div class="diamond" style="left:565px;top:236px"></div>
    <h3 style="left:678px;top:220px">Franchise development<br>and launch</h3>
    <p style="left:678px;top:278px;width:425px">At Vellowind Advisory, our Franchise Development &amp; Launch service is designed to transform your successful business into a thriving franchise. We start by thoroughly evaluating your business model to determine its franchisability. Once confirmed, our team handles every aspect of the franchise setup, including legal documentation, branding, marketing strategies, operational guidelines, and franchisee recruitment.<br><br>Our goal is to ensure a seamless and efficient transition from a single successful location to a robust franchise network, empowering your business to scale effectively and achieve exponential growth. Partner with us to turn your business into a nationwide brand.</p>
  </div>

  <div class="svc">
    <h3 style="left:100px;top:612px;width:422px;text-align:right">Due Diligence Services</h3>
    <p style="left:96px;top:650px;width:426px;text-align:right">Vellowind offers comprehensive evaluations tailored to your business needs. We meticulously assess franchise opportunities, business sales, and property transactions, identifying potential risks and liabilities to safeguard your investments. Our expert team provides actionable recommendations on deal points and offers strategic guidance throughout the entire process.<br><br>Whether you're exploring new ventures or expanding your portfolio, trust us to deliver detailed insights and informed advice, ensuring you make confident, well-informed decisions. Partner with us for thorough due diligence that supports your success and minimizes uncertainties in any deal.</p>
    <div class="diamond dark" style="left:565px;top:630px"></div>
    <div class="ring" style="left:694px;top:566px;width:372px;height:372px"></div>
    <div class="circle-img" style="left:707px;top:579px;width:346px;height:346px;background:radial-gradient(circle,#3b5a57,#1d2d2e 70%);border:12px solid var(--mint)" role="img" aria-label="Illustration of a circular dashboard of due diligence icons"></div>
  </div>

  <div class="svc">
    <div class="ring" style="left:170px;top:960px;width:372px;height:372px"></div>
    <div class="circle-img" style="left:185px;top:975px;width:342px;height:342px;background:linear-gradient(135deg,#c9d3da,#e9edf0 50%,#7f8b93)" role="img" aria-label="Photo of engineers reviewing construction plans with a hard hat on the desk"></div>
    <div class="diamond" style="left:565px;top:971px"></div>
    <h3 style="left:678px;top:958px">Construction Management</h3>
    <p style="left:680px;top:998px;width:430px">Our Building &amp; Construction Management Services oversee every aspect of your construction and development projects, from initial planning to final completion. We ensure projects stay on time and within budget, providing meticulous attention to detail and proactive problem-solving.<br><br>Specializing in tenant improvements (TIs) and ground-up construction for small to mid-size commercial projects, we handle everything from permitting and contractor coordination to quality control and final inspections. Trust us to deliver successful projects that meet your specifications and exceed your expectations, ensuring a smooth and efficient construction process every step of the way.</p>
  </div>
</section>

<section class="contact" role="img" aria-label="Darkened photo of a commercial building exterior">
  <svg class="abs" style="left:0;top:0" width="1200" height="80" viewBox="0 0 1200 80">
    <polygon points="0,0 1200,0 1200,75 600,0 0,65" fill="#fff"/>
    <polygon points="0,65 600,0 600,8 0,76" fill="#8fc5a8"/>
  </svg>
  <div class="eyebrow abs center" style="text-align:center">Get in touch</div>
  <h2 class="h2 abs center" style="text-align:center">Contact Vellowind</h2>

  <div class="info" style="top:254px">
    <div class="ic"><svg width="26" height="30" viewBox="0 0 26 30"><path d="M13 1C6.4 1 2 5.8 2 11.6 2 19 13 29 13 29s11-10 11-17.4C24 5.8 19.6 1 13 1z" fill="#fff"/><circle cx="13" cy="11.5" r="4" fill="#8fc5a8"/></svg></div>
    <div><h4>Address</h4><span>410 Meridian Way,<br>Harlow Springs, CA 90210</span></div>
  </div>
  <div class="info" style="top:370px">
    <div class="ic"><svg width="30" height="22" viewBox="0 0 30 22"><rect x="1" y="1" width="28" height="20" rx="2" fill="#fff"/><path d="M2 2l13 11L28 2" fill="none" stroke="#8fc5a8" stroke-width="2"/></svg></div>
    <div><h4>Email Us</h4><span>enquiry@vellowindadvisory.example</span></div>
  </div>
  <div class="info" style="top:464px">
    <div class="ic"><svg width="28" height="28" viewBox="0 0 24 24"><path d="M6.6 10.8a15 15 0 006.6 6.6l2.2-2.2a1 1 0 011-.25 11.4 11.4 0 003.6.6 1 1 0 011 1V20a1 1 0 01-1 1A17 17 0 013 4a1 1 0 011-1h3.5a1 1 0 011 1 11.4 11.4 0 00.6 3.6 1 1 0 01-.25 1z" fill="#fff"/></svg></div>
    <div><h4>Phone number</h4><span>(555) 014 2290</span></div>
  </div>

  <form class="form">
    <div class="field" style="left:47px;top:76px;width:210px">First Name</div>
    <div class="field" style="left:265px;top:76px;width:210px">Last Name</div>
    <div class="field" style="left:47px;top:132px;width:210px">Email address</div>
    <div class="field" style="left:265px;top:132px;width:210px">Phone</div>
    <div class="field" style="left:47px;top:186px;width:428px;height:88px">Leave message</div>
    <div class="send">SEND MESSAGE</div>
  </form>
</section>

<footer class="footer">
  <div class="brand abs" style="left:126px;top:56px;font-size:20px"><i style="width:68px;height:68px"></i>Vellowind<br>Advisory</div>
  <p class="abs" style="left:136px;top:152px;font-size:12.5px;line-height:19px;color:var(--ink)">© 2024 Vellowind Advisory<br>All Right Reserved</p>
  <div class="vrule" style="left:384px"></div>
  <h5 style="left:413px">Navigation</h5>
  <ul style="left:416px;top:98px"><li style="text-decoration:underline">Home</li><li>About Us</li><li>Team</li><li>Services</li><li>Contact Us</li></ul>
  <div class="vrule" style="left:592px"></div>
  <h5 style="left:616px">Contact Us</h5>
  <div class="frow" style="left:618px;top:104px"><i></i>410 Meridian Way, Harlow Springs, CA 90210</div>
  <div class="frow" style="left:618px;top:150px"><i></i>(555) 014 2290</div>
  <div class="frow" style="left:618px;top:196px"><i></i>enquiry@vellowindadvisory.example</div>
  <div class="vrule" style="left:900px"></div>
  <h5 style="left:925px">Follow us</h5>
  <div class="social"><i></i><i></i><i></i></div>
</footer>

</body>
</html>
```